Thornfield Marsh, LLC Website

We are a small law firm in need of a website that contains the following:
1. Attractive main page
2. About us/attorney info for three people: Leonard Thornfield (attorney), Brent Marsh (attorney), and Melinda Carrow (legal assistant). We have bio's ready to submit.
3. Blog/video page. We'd like to post blogs and videos to help drive traffic
4. Multidistrict Litigation and Class Actions page, where we post information regarding active MDLs and Class actions that we are doing intake on.
Updates

Can you also please use the color "gold" in the design and logo? Thanks.

Industry/Entity Type

Legal

Coding

Coded - Design and coding required

Number of Pages Required

1 page

Colors
0054AA
0677BA
7BADD7
CADEEF
E8F1F8

Requirements
Must have
• 1. Attractive main page 2. About us/attorney info for three people: Leonard Thornfield (attorney), Brent Marsh (attorney), and Melinda Carrow (legal assistant). We have bio's ready to submit. 3. Blog/video page. We'd like to post blogs and videos to help drive traffic 4. Multidistrict Litigation and Class Actions page, where we post information regarding active MDLs and Class actions that we are doing intake on.

```html
<!DOCTYPE html>
<html lang="en">
<head>
<meta charset="utf-8">
<title>Thornfield Marsh, LLC — Website Presentation</title>
<link href="https://fonts.googleapis.com/css2?family=Prata&family=Mulish:wght@400;600;700;800&display=swap" rel="stylesheet">
<style>
:root{
  --ink:#1d2230;
  --hero:#2c3342;
  --hero-deep:#1f2533;
  --accent:#5aa9d6;
  --button:#6cb4df;
  --light:#f6f6f4;
  --warm:#ecebe7;
  --soft:#a9d2ec;
  --muted:#7b8088;
  --rule:#e2e2df;
  --navy:#0b1585;
  --cyan:#12b0ee;
  --footer:#c4ddef;
  --gold:#c8a25a;
}
*{margin:0;padding:0;box-sizing:border-box}
html,body{width:1200px;height:1200px;overflow:hidden;background:#fff}
body{font-family:"Mulish",sans-serif;color:var(--ink)}
.board{position:relative;width:1200px;height:1200px;overflow:hidden;background:#fff}
.abs{position:absolute}
.serif{font-family:"Prata",serif;font-weight:400}
.ph{position:absolute}

/* ---------- page overview strip ---------- */
.strip{position:absolute;left:0;top:0;width:194px;height:1200px;overflow:hidden}
.strip .sec{position:absolute;left:0;width:194px;overflow:hidden}
.tiny{font-size:3px;line-height:4.2px;color:var(--muted)}
.kick{font-size:2.4px;letter-spacing:.3px;font-weight:700;text-transform:uppercase}
.tbtn{position:absolute;height:7px;background:var(--button);color:#fff;font-size:2.2px;font-weight:700;letter-spacing:.3px;display:flex;align-items:center;justify-content:center}

/* ---------- hero ---------- */
.hero{position:absolute;left:224px;top:0;width:701px;height:461px;overflow:hidden;color:#fff}
.hero-photo{left:0;top:0;width:701px;height:461px;background:
  radial-gradient(ellipse 180px 260px at 430px 250px,#6f7683 0%,rgba(80,88,102,.6) 45%,rgba(44,51,66,0) 80%),
  radial-gradient(ellipse 110px 70px at 640px 230px,rgba(200,162,90,.55),rgba(0,0,0,0) 70%),
  linear-gradient(180deg,#3a4252 0%,#2c3342 60%,#1f2533 100%)}
.nav-brand{left:36px;top:8px;height:26px;display:flex;align-items:center;gap:6px;font-weight:800;font-size:12px;letter-spacing:.4px;color:#fff}
.nav-brand .mark{width:14px;height:14px;background:var(--cyan)}
.nav{left:247px;top:14px;display:flex;gap:15px;font-size:8.4px;color:#e9ecf2}
.nav span:first-child{color:#a8afbb}
.cta{left:576px;top:8px;width:89px;height:25px;background:var(--button);font-size:6.2px;font-weight:700;letter-spacing:1px;display:flex;align-items:center;justify-content:center}
.nav-rule{left:36px;top:46px;width:629px;height:1px;background:rgba(255,255,255,.25)}
.headline{left:36px;top:104px;font-size:37px;line-height:33px;letter-spacing:-.5px}
.headline em{font-style:normal;color:var(--accent)}
.stat{left:184px;top:318px;font-size:76px;line-height:76px;color:var(--accent)}
.stat-note{left:261px;top:356px;font-size:11.5px;line-height:15px;width:110px}
.hero-note{left:435px;top:359px;font-size:9.2px;line-height:14.5px;width:215px;color:#e6e9ee}

/* ---------- services ---------- */
.services{position:absolute;left:224px;top:461px;width:701px;height:365px;background:var(--light)}
.col-rule{top:0;width:1px;height:365px;background:var(--rule)}
.label{font-size:6.6px;font-weight:700;letter-spacing:1.4px;text-transform:uppercase;color:var(--ink)}
.svc-title{left:20px;top:91px;font-size:22px;line-height:25px;width:130px}
.svc-copy{left:20px;top:181px;width:125px;font-size:8.3px;line-height:13.2px;color:var(--muted)}
.btn{background:var(--button);color:#fff;font-weight:700;font-size:7px;letter-spacing:1.4px;display:flex;align-items:center;justify-content:center;text-transform:uppercase}
.card{width:134px}
.card .img{width:134px;height:140px}
.card h3{margin-top:13px;font-size:10.5px}
.card p{margin-top:7px;font-size:8.2px;line-height:13.2px;color:var(--muted)}

/* ---------- about ---------- */
.about-img{left:296px;top:902px;width:271px;height:310px;background:linear-gradient(90deg,#b9b3a8 0%,#d9d4cb 18%,#6f6659 32%,#4a4238 50%,#8a8074 68%,#d6d1c8 85%,#b3ada2 100%)}
.about-kick{left:622px;top:902px}
.about-title{left:622px;top:918px;font-size:22px;line-height:29px;white-space:nowrap}
.about-art{left:652px;top:998px;width:200px;height:102px;background:radial-gradient(ellipse at center,#eef0f2 0%,#f8f9fa 60%,rgba(255,255,255,0) 100%)}
.about-rule{left:622px;top:1120px;width:232px;height:1px;background:var(--rule)}
.about-copy{left:622px;top:1136px;width:232px;font-size:8.3px;line-height:13.2px;color:var(--muted)}

/* ---------- brand tile ---------- */
.brand-tile{left:1045px;top:319px;width:101px;height:569px;background:var(--navy);display:flex;align-items:center;justify-content:center}
.brand-tile span{transform:rotate(-90deg);white-space:nowrap;color:#fff;font-weight:800;font-size:26px;letter-spacing:1px}
</style>
</head>
<body>
<div class="board">

  <!-- ===== full page overview ===== -->
  <div class="strip">
    <section class="sec" style="top:0;height:128px;background:var(--hero)">
      <div class="ph" role="img" aria-label="Attorney portrait with gavel" style="left:60px;top:0;width:134px;height:128px;background:radial-gradient(ellipse 50px 80px at 60px 70px,#6f7683,rgba(44,51,66,0) 80%)"></div>
      <div class="abs" style="left:10px;top:3px;width:5px;height:5px;background:var(--cyan)"></div>
      <div class="abs" style="left:17px;top:3px;font-size:3px;font-weight:800;color:#fff">THORNFIELD MARSH</div>
      <div class="abs" style="left:68px;top:4px;font-size:2.2px;color:#dfe3ea;display:flex;gap:4px"><span>Home</span><span>About</span><span>Multidistrict</span><span>Class Action</span><span>Blog</span><span>Contact</span></div>
      <div class="abs" style="left:160px;top:2px;width:24px;height:7px;background:var(--button)"></div>
      <div class="abs serif" style="left:10px;top:30px;font-size:9.5px;line-height:9px;color:#fff">FOCUSED<br>ADVOCACY FOR<br>YOUR <span style="color:var(--accent)">LEGAL</span><br>SUCCESS</div>
      <div class="abs" style="left:12px;top:82px;width:32px;height:32px;border:1px dashed rgba(255,255,255,.5);border-radius:50%"></div>
      <div class="abs serif" style="left:50px;top:88px;font-size:19px;color:var(--accent)">12</div>
      <div class="abs serif" style="left:72px;top:98px;font-size:2.8px;line-height:3.6px;color:#fff">Years of success in<br>legal advocacy</div>
      <div class="abs" style="left:120px;top:99px;font-size:2.2px;line-height:3.2px;color:#e6e9ee">Expert legal guidance protecting your rights and<br>delivering justice with dedication and integrity</div>
    </section>

    <section class="sec" style="top:128px;height:101px;background:var(--light)">
      <div class="abs kick" style="left:6px;top:21px">What we do</div>
      <div class="abs serif" style="left:6px;top:26px;font-size:5.4px;line-height:6.2px">Supporting<br>Your Legal<br>Journey</div>
      <div class="abs tiny" style="left:6px;top:50px;width:36px;font-size:2.2px;line-height:3px">Thornfield Marsh, LLC provides tailored legal solutions to empower clients in navigating complex legal landscapes.</div>
      <div class="tbtn" style="left:6px;top:73px;width:29px">MORE SERVICES</div>
      <div class="ph" role="img" aria-label="Bronze justice statue" style="left:54px;top:21px;width:38px;height:39px;background:linear-gradient(160deg,#a49a88,#6e6150)"></div>
      <div class="ph" role="img" aria-label="Hands signing a contract" style="left:102px;top:21px;width:38px;height:39px;background:linear-gradient(160deg,#c9b8a4,#6b4a32)"></div>
      <div class="ph" role="img" aria-label="Wedding rings on wet stone" style="left:151px;top:21px;width:38px;height:39px;background:linear-gradient(160deg,#5b6c72,#2f3a3f)"></div>
      <div class="abs serif" style="left:54px;top:64px;font-size:2.6px">Legal Expertise</div>
      <div class="abs serif" style="left:102px;top:64px;font-size:2.6px">Corporate Law</div>
      <div class="abs serif" style="left:151px;top:64px;font-size:2.6px">Family Law</div>
      <div class="abs tiny" style="left:54px;top:69px;width:36px;font-size:2px;line-height:2.8px">Helping businesses navigate corporate law complexities.</div>
      <div class="abs tiny" style="left:102px;top:69px;width:36px;font-size:2px;line-height:2.8px">Protect your innovations with our intellectual property services.</div>
      <div class="abs tiny" style="left:151px;top:69px;width:36px;font-size:2px;line-height:2.8px">Thornfield Marsh offers compassionate representation in family law matters.</div>
    </section>

    <section class="sec" style="top:229px;height:131px;background:#fff">
      <div class="ph" role="img" aria-label="Lawyer standing between stone columns" style="left:20px;top:22px;width:75px;height:88px;background:linear-gradient(90deg,#bdb7ac,#6e6558 45%,#cfc9bf)"></div>
      <div class="abs kick" style="left:110px;top:22px">Upholding justice</div>
      <div class="abs serif" style="left:110px;top:27px;font-size:6px;line-height:7px">We develop &amp; create<br>legal solutions</div>
      <div class="abs" style="left:110px;top:80px;width:64px;height:1px;background:var(--rule)"></div>
      <div class="abs tiny" style="left:110px;top:84px;width:64px;font-size:2px;line-height:2.8px">At Thornfield Marsh, LLC we are committed to delivering exceptional legal services tailored to our clients' needs.</div>
      <div class="tbtn" style="left:110px;top:102px;width:36px">OUR LEGAL SERVICES</div>
    </section>

    <section class="sec" style="top:360px;height:168px;background:#f4f5f7">
      <div class="abs kick" style="left:20px;top:20px">Legal expertise</div>
      <div class="abs serif" style="left:20px;top:26px;font-size:5.8px;line-height:8px">Delivering exceptional legal services<br>is our <span style="color:var(--accent)">driving force behind our firm</span><br>and our commitment to clients</div>
      <div class="abs tiny" style="left:99px;top:56px;width:75px;font-size:2px;line-height:2.8px">We are committed to delivering outstanding legal services, ensuring our clients receive tailored solutions that empower them to face every legal challenge with confidence.</div>
      <div class="abs" style="left:20px;top:83px;width:49px;height:64px;background:#fff"></div>
      <div class="abs" style="left:73px;top:83px;width:48px;height:64px;background:var(--button)"></div>
      <div class="abs" style="left:126px;top:83px;width:48px;height:64px;background:var(--soft)"></div>
      <div class="abs serif" style="left:25px;top:110px;font-size:3.4px;line-height:4px">Legal<br>Expertise</div>
      <div class="abs serif" style="left:78px;top:110px;font-size:3.4px;line-height:4px;color:#fff">Expert<br>Strategies</div>
      <div class="abs serif" style="left:131px;top:110px;font-size:3.4px;line-height:4px;color:#1f5f8a">Tailored Legal<br>Solutions</div>
      <div class="abs tiny" style="left:25px;top:125px;width:40px;font-size:1.9px;line-height:2.6px">We specialize in providing exceptional legal services tailored to your needs.</div>
      <div class="abs tiny" style="left:78px;top:125px;width:40px;font-size:1.9px;line-height:2.6px;color:#eef6fb">We offer specialized legal services, including corporate, family and IP law.</div>
      <div class="abs tiny" style="left:131px;top:125px;width:40px;font-size:1.9px;line-height:2.6px;color:#1f5f8a">Our legal services encompass corporate, family and intellectual property law.</div>
    </section>

    <section class="sec" style="top:528px;height:135px;background:var(--warm)">
      <div class="ph" role="img" aria-label="Two judges in robes on courthouse steps" style="left:10px;top:21px;width:85px;height:93px;background:linear-gradient(160deg,#ddd8cf,#3a3633 70%)"></div>
      <div class="abs serif" style="left:109px;top:22px;font-size:3.4px;line-height:4px">Empowering clients through<br>legal expertise</div>
      <div class="abs serif" style="left:109px;top:46px;font-size:4.6px;line-height:11px">Corporate Law<br><span style="color:var(--accent)">Family Law</span><br><span style="color:var(--accent)">Intellectual Property</span></div>
      <div class="abs serif" style="left:109px;top:101px;font-size:2.4px">Tailored legal solutions for success</div>
      <div class="abs tiny" style="left:109px;top:105px;width:68px;font-size:1.9px;line-height:2.6px">Thornfield Marsh, LLC provides expert legal support in corporate, family, and intellectual property law.</div>
    </section>

    <section class="sec" style="top:663px;height:118px;background:var(--hero)">
      <div class="abs kick" style="left:20px;top:21px;color:#cfd5de">Meet our team</div>
      <div class="abs serif" style="left:20px;top:26px;font-size:6px;color:#fff">Our Leaders</div>
      <div class="abs tiny" style="left:20px;top:40px;width:46px;font-size:2.2px;line-height:3px;color:#cfd5de">We're 120+ professionals dedicated to legal excellence</div>
      <div class="ph" role="img" aria-label="Portrait of Leonard Thornfield" style="left:73px;top:21px;width:49px;height:65px;background:linear-gradient(180deg,#3b4a66,#1d2739)"></div>
      <div class="ph" role="img" aria-label="Portrait of Brent Marsh" style="left:126px;top:21px;width:48px;height:65px;background:linear-gradient(180deg,#4a5568,#232a38)"></div>
      <div class="abs" style="left:73px;top:91px;font-size:2.2px;line-height:3px;color:#dfe3ea">Leonard Thornfield<br><span style="color:#9aa3b0">Senior partner</span></div>
      <div class="abs" style="left:126px;top:91px;font-size:2.2px;line-height:3px;color:#dfe3ea">Brent Marsh<br><span style="color:#9aa3b0">Senior partner</span></div>
    </section>

    <section class="sec" style="top:781px;height:80px;background:#17191d">
      <div class="abs serif" style="left:0;top:0;width:194px;text-align:center;font-size:3.8px;line-height:5px;color:#e6e9ee">Thornfield Marsh, LLC committed attorneys<br>serving clients nationwide</div>
      <div class="abs" style="left:20px;top:15px;width:35px;height:42px;background:#23262b"></div>
      <div class="abs" style="left:60px;top:15px;width:35px;height:42px;background:#23262b"></div>
      <div class="abs" style="left:99px;top:15px;width:36px;height:42px;background:#23262b"></div>
      <div class="abs" style="left:139px;top:15px;width:35px;height:42px;background:#23262b"></div>
    </section>

    <section class="sec" style="top:861px;height:136px;background:#efede9">
      <div class="abs kick" style="left:0;top:22px;width:194px;text-align:center">Client testimonials</div>
      <div class="abs serif" style="left:0;top:26px;width:194px;text-align:center;font-size:6px;line-height:8px">We offer tailored legal<br>solutions</div>
      <div class="abs" style="left:20px;top:49px;width:75px;height:51px;background:#fff"></div>
      <div class="abs" style="left:99px;top:49px;width:75px;height:51px;background:#fff"></div>
      <div class="abs" style="left:25px;top:55px;font-size:3px;color:var(--gold)">★★★★★</div>
      <div class="abs" style="left:104px;top:55px;font-size:3px;color:var(--gold)">★★★★★</div>
      <div class="abs tiny" style="left:25px;top:62px;width:66px;font-size:1.9px;line-height:2.6px;color:#333">Thornfield Marsh, LLC transformed my business, skillfully guiding us through intricate legal challenges. Their expertise is unparalleled.</div>
      <div class="abs tiny" style="left:104px;top:62px;width:66px;font-size:1.9px;line-height:2.6px;color:#333">Thornfield Marsh, LLC legal expertise empowered me to overcome business challenges effectively. Their support was invaluable.</div>
      <div class="abs" style="left:25px;top:88px;width:7px;height:7px;border-radius:50%;background:#c9ccd2"></div>
      <div class="abs" style="left:104px;top:88px;width:7px;height:7px;border-radius:50%;background:#c9ccd2"></div>
      <div class="abs" style="left:35px;top:89px;font-size:1.9px;line-height:2.6px;color:#333">Owen Harlow<br><span style="color:var(--accent)">Operations Manager</span></div>
      <div class="abs" style="left:114px;top:89px;font-size:1.9px;line-height:2.6px;color:#333">Nora Ellis<br><span style="color:var(--accent)">Brand Strategist</span></div>
      <div class="tbtn" style="left:83px;top:107px;width:28px;background:#1b1d22">GET IN TOUCH</div>
    </section>

    <section class="sec" style="top:997px;height:131px;background:#fff">
      <div class="abs kick" style="left:20px;top:22px;color:var(--accent)">Discover Thornfield Marsh, LLC</div>
      <div class="abs serif" style="left:99px;top:22px;font-size:6px;line-height:8px">Latest news and insights<br>from the legal sector</div>
      <div class="ph" role="img" aria-label="Woman reading documents" style="left:20px;top:43px;width:48px;height:36px;background:linear-gradient(160deg,#e6e2dc,#9aa0a8)"></div>
      <div class="ph" role="img" aria-label="Classical courthouse facade" style="left:73px;top:43px;width:48px;height:43px;background:linear-gradient(180deg,#f1e4cf,#b88f5c)"></div>
      <div class="ph" role="img" aria-label="Gavel on dark desk" style="left:126px;top:43px;width:48px;height:38px;background:linear-gradient(160deg,#8c8f94,#2a2c30)"></div>
      <div class="abs" style="left:20px;top:84px;font-size:1.8px;font-weight:700">LAW FIRM</div>
      <div class="abs serif" style="left:20px;top:87px;width:46px;font-size:2.6px;line-height:3.3px;color:#2a67a8">Common legal mistakes and how to avoid them</div>
      <div class="abs" style="left:73px;top:91px;font-size:1.8px;font-weight:700">LAW FIRM</div>
      <div class="abs serif" style="left:73px;top:94px;width:46px;font-size:2.6px;line-height:3.3px;color:#2a67a8">How to market a law firm effectively</div>
      <div class="abs" style="left:126px;top:86px;font-size:1.8px;font-weight:700">LAW FIRM</div>
      <div class="abs serif" style="left:126px;top:89px;width:46px;font-size:2.6px;line-height:3.3px;color:#2a67a8">The importance of contracts in business law</div>
    </section>

    <section class="sec" style="top:1128px;height:72px;background:var(--footer)">
      <div class="abs" style="left:20px;top:15px;width:5px;height:5px;background:var(--navy)"></div>
      <div class="abs" style="left:27px;top:15px;font-size:3px;font-weight:800;color:var(--navy)">THORNFIELD MARSH</div>
      <div class="abs" style="left:60px;top:13px;font-size:2px;line-height:3.2px;color:#2a67a8">Office<br><br>USA —<br>48 Elm Street, Office 12<br>Fairhaven, AL 36000<br><br>hello@thornfieldmarsh.law<br><br>+1 (555) 014-2290</div>
      <div class="abs" style="left:99px;top:13px;font-size:2px;line-height:3.2px;color:#2a67a8">Links<br><span style="color:#333">Home<br>About Us<br>Multidistrict Litigation<br>Class Actions<br>Blog<br>Contacts</span></div>
      <div class="abs" style="left:139px;top:13px;font-size:2px;color:#2a67a8">Social Media</div>
      <div class="abs" style="left:139px;top:18px;display:flex;gap:2px"><i style="width:5px;height:5px;border:.4px solid #2a67a8;border-radius:50%"></i><i style="width:5px;height:5px;border:.4px solid #2a67a8;border-radius:50%"></i><i style="width:5px;height:5px;border:.4px solid #2a67a8;border-radius:50%"></i><i style="width:5px;height:5px;border:.4px solid #2a67a8;border-radius:50%"></i></div>
      <div class="abs" style="left:20px;top:65px;font-size:1.8px;color:#333">© 2025 Thornfield Marsh, LLC All Rights Reserved.</div>
      <div class="abs" style="left:160px;top:65px;font-size:1.8px;color:#333">Privacy Policy</div>
    </section>
  </div>

  <!-- ===== hero ===== -->
  <section class="hero">
    <div class="ph hero-photo" role="img" aria-label="Smiling attorney in a grey suit with a gavel in the foreground"></div>
    <div class="abs nav-brand"><span class="mark"></span>THORNFIELD MARSH</div>
    <nav class="abs nav"><span>Home</span><span>About</span><span>Multidistrict Litigation</span><span>Class Action</span><span>Blog</span><span>Contact</span></nav>
    <div class="abs cta">CONSULTATION</div>
    <div class="abs nav-rule"></div>
    <h1 class="abs serif headline">FOCUSED<br>ADVOCACY FOR<br>YOUR <em>LEGAL</em><br>SUCCESS</h1>
    <svg class="abs" style="left:36px;top:292px" width="128" height="128" viewBox="0 0 128 128">
      <circle cx="64" cy="64" r="63" fill="none" stroke="rgba(255,255,255,.3)" stroke-width=".8"/>
      <defs><path id="ring" d="M64,64 m-48,0 a48,48 0 1,1 96,0 a48,48 0 1,1 -96,0"/></defs>
      <text font-family="Mulish,sans-serif" font-size="6.6" font-weight="700" letter-spacing="1.3" fill="#fff"><textPath href="#ring">VIEW PRESENTATION  –  VIEW PRESENTATION  –  VIEW PRESENTAT</textPath></text>
      <path d="M60,58 L68,64 L60,70 Z" fill="#fff"/>
    </svg>
    <div class="abs serif stat">12</div>
    <div class="abs serif stat-note">Years of success in legal advocacy</div>
    <p class="abs hero-note">Expert legal guidance protecting your rights and delivering justice with dedication and integrity</p>
  </section>

  <!-- ===== services ===== -->
  <section class="services">
    <div class="abs col-rule" style="left:175px"></div>
    <div class="abs col-rule" style="left:350px"></div>
    <div class="abs col-rule" style="left:526px"></div>
    <div class="abs label" style="left:20px;top:75px">What we do</div>
    <h2 class="abs serif svc-title">Supporting Your Legal Journey</h2>
    <p class="abs svc-copy">Thornfield Marsh, LLC provides tailored legal solutions to empower clients in navigating complex legal landscapes.</p>
    <div class="abs btn" style="left:20px;top:261px;width:109px;height:28px">More services</div>
    <div class="abs card" style="left:196px;top:76px">
      <div class="img" role="img" aria-label="Bronze statue of Lady Justice holding scales" style="background:linear-gradient(160deg,#b4ab9c,#8a7c66 55%,#5e5344)"></div>
      <h3 class="serif">Legal Expertise</h3>
      <p>Helping businesses navigate corporate law complexities.</p>
    </div>
    <div class="abs card" style="left:371px;top:76px">
      <div class="img" role="img" aria-label="Hands signing a contract on a wooden desk" style="background:linear-gradient(160deg,#e2d8cc,#a27a58 55%,#5f3f27)"></div>
      <h3 class="serif">Corporate Law</h3>
      <p>Protect your innovations with our intellectual property services.</p>
    </div>
    <div class="abs card" style="left:546px;top:76px">
      <div class="img" role="img" aria-label="Two wedding rings on a wet dark surface" style="background:linear-gradient(160deg,#6c7c82,#3c484d 60%,#2a3236)"></div>
      <h3 class="serif">Family Law</h3>
      <p>Thornfield Marsh offers compassionate representation in family law matters.</p>
    </div>
  </section>

  <!-- ===== about ===== -->
  <div class="ph about-img" role="img" aria-label="Lawyer checking his phone between courthouse columns"></div>
  <div class="abs label about-kick">Upholding justice</div>
  <h2 class="abs serif about-title">We develop &amp; create<br>legal solutions</h2>
  <div class="ph about-art" role="img" aria-label="Faint line sketch of a gavel resting on law books"></div>
  <div class="abs about-rule"></div>
  <p class="abs about-copy">At Thornfield Marsh, LLC we are committed to delivering exceptional legal services tailored to our clients' needs, working diligently to achieve the best outcomes.</p>
  <div class="abs btn" style="left:622px;top:1193px;width:132px;height:28px">Our legal services</div>

  <!-- ===== brand tile ===== -->
  <div class="abs brand-tile"><span>THORNFIELD MARSH, LLC</span></div>

</div>
</body>
</html>
```